Web Design Project - brivocell

I'm building an agency for marketing solutions but also medical education and patients education for pharmaceutical companies, medical societies and patient advocacy groups. We want to be perceived as the most innovative in the market. We work through design thinking solutions for campaigns and services.
I love some websites based on Swiss style design like www.plumvane.example
We are a small group of designers, physicians and creatives working together to deliver the best experiences in our market.
We decided to also use pixel forum expecting that we maybe found a great idea we didn't thought about yet.

I'm extending it for more 2 weeks

Reason: I need the best design you can. Only PSD. No code needed. Love Swiss style, like tessera 5 and plumvane.example I'm extending the deadline until get something great. Willing to extend as much as needed.

Target Market(s)

Pharmaceutical companies, physicians, medical societies, patients advocacy groups

Industry/Entity Type

Pharmaceutical

Font styles to use
Other font styles liked:
• Helvetia family

Colors

Designer to choose colors to be used in the design.

Requirements
Must have
• Must be innovative like www.plumvane.example
Nice to have
• Cool menus
Should not have
• Not to appear too much Comercial. We like to be a boutique in this market. Craftsmen working with less clients at time but delivering precious stones.

```html
<!DOCTYPE html>
<html lang="en">
<head>
<meta charset="utf-8">
<title>brivocell</title>
<link rel="stylesheet" href="https://fonts.googleapis.com/css2?family=Abel&family=Open+Sans:wght@400;700&display=swap">
<style>
  :root {
    --pink: #e0517b;
    --teal: #00c5be;
    --purple: #8a6aab;
    --white: #ffffff;
    --ink: #ffffff;
    --page: #ffffff;
  }
  * { box-sizing: border-box; margin: 0; padding: 0; }
  html, body { width: 910px; height: 1200px; overflow: hidden; }
  body { position: relative; background: var(--page); font-family: "Open Sans", Arial, sans-serif; color: var(--ink); }

  .site-header { position: absolute; left: 0; top: 0; width: 910px; height: 53px; background: var(--pink); }
  .brand { position: absolute; left: 106px; top: 11px; font-weight: 700; font-size: 22px; color: var(--white); letter-spacing: 0.2px; }
  .main-nav { position: absolute; left: 376px; top: 9px; display: flex; gap: 10px; }
  .main-nav a { display: block; width: 33px; height: 33px; }
  .main-nav svg { width: 33px; height: 33px; display: block; }
  .phone { position: absolute; right: 92px; top: 14px; font-weight: 700; font-size: 17px; color: var(--white); display: flex; align-items: center; gap: 16px; }

  .hero { position: absolute; left: 0; top: 53px; width: 910px; height: 432px;
    background: linear-gradient(180deg, #4f7ea3 0%, #5d8aac 55%, #6b94b2 70%, #b9c8cf 80%, #a2895e 86%, #8d7650 100%); }

  .tagline { position: absolute; left: 0; top: 485px; width: 910px; height: 91px; background: var(--teal);
    font-family: "Abel", "Arial Narrow", sans-serif; font-size: 28px; line-height: 37px; text-align: center; color: var(--white);
    padding-top: 9px; letter-spacing: 0.6px; }

  .services { position: absolute; left: 106px; top: 576px; width: 696px; height: 410px;
    display: grid; grid-template-columns: repeat(3, 232px); grid-template-rows: repeat(2, 205px); }
  .photo { width: 232px; height: 205px; }
  .photo-pills { background: linear-gradient(135deg, #e9e4dc 0%, #f3efe8 40%, #e8a86a 65%, #e77ab8 100%); }
  .photo-scope { background: linear-gradient(160deg, #3a3532 0%, #5c5550 50%, #8d8884 100%); }
  .photo-doctor { background: linear-gradient(180deg, #e8ebef 0%, #cfd6dd 60%, #c7a58e 100%); }

  .service { position: relative; width: 232px; height: 205px; text-align: center; padding: 0 18px; }
  .service h2 { font-family: "Abel", "Arial Narrow", sans-serif; font-weight: 400; font-size: 22px; line-height: 27px; letter-spacing: 0.5px; }
  .service .rule { width: 52px; height: 1px; background: rgba(255,255,255,0.75); margin: 10px auto 14px; }
  .service p { font-size: 10px; line-height: 13px; }
  .service .more { display: inline-block; margin-top: 12px; font-family: "Abel", "Arial Narrow", sans-serif; font-size: 11px; color: var(--white); text-decoration: underline; letter-spacing: 0.4px; }
  .service-patients { background: var(--pink); padding-top: 27px; }
  .service-pharma { background: var(--teal); padding-top: 24px; }
  .service-societies { background: var(--purple); padding-top: 24px; }
  .pointer { position: absolute; left: 50%; width: 0; height: 0; margin-left: -15px; border-left: 15px solid transparent; border-right: 15px solid transparent; }
  .pointer-down { bottom: -15px; border-top: 15px solid var(--pink); z-index: 2; }
  .pointer-up-teal { top: -15px; border-bottom: 15px solid var(--teal); }
  .pointer-up-purple { top: -15px; border-bottom: 15px solid var(--purple); }

  .footer-tab { position: absolute; left: 338px; top: 1085px; width: 233px; height: 42px; background: var(--purple);
    font-weight: 700; font-size: 33px; line-height: 46px; text-align: center; color: var(--white); }
  .site-footer { position: absolute; left: 0; top: 1126px; width: 910px; height: 74px; background: var(--purple); font-size: 12px; }
  .address { position: absolute; left: 106px; top: 22px; }
  .legal { position: absolute; left: 0; width: 910px; top: 22px; text-align: center; line-height: 16px; }
  .social { position: absolute; right: 108px; top: 22px; display: flex; gap: 2px; }
  .social span { display: block; width: 27px; height: 27px; }
  .social .s1 { background: #3b5a98; }
  .social .s2 { background: #29a8e0; }
  .social .s3 { background: #dc4a38; }
  .social .s4 { background: #c4302b; }
</style>
</head>
<body>
  <header class="site-header">
    <div class="brand">brivocell</div>
    <nav class="main-nav">
      <a aria-label="Home"><svg viewBox="0 0 33 33" fill="none" stroke="#fff" stroke-width="1.6"><circle cx="16.5" cy="16.5" r="15.5"/><path d="M9 17 L16.5 10 L24 17 M11.5 15 V23 H15 V19 H18 V23 H21.5 V15"/></svg></a>
      <a aria-label="About"><svg viewBox="0 0 33 33" fill="none" stroke="#fff" stroke-width="1.6"><circle cx="16.5" cy="16.5" r="15.5"/><circle cx="17" cy="10.5" r="1.2" fill="#fff"/><path d="M15 14.5 H17.5 L16 23 H18.5"/></svg></a>
      <a aria-label="Services"><svg viewBox="0 0 33 33" fill="none" stroke="#fff" stroke-width="1.6"><circle cx="16.5" cy="16.5" r="15.5"/><path d="M12 9 L14 19 H20 L22 24 M14 19 L13 24 M15 14 H19"/></svg></a>
      <a aria-label="Contact"><svg viewBox="0 0 33 33" fill="none" stroke="#fff" stroke-width="1.6"><circle cx="16.5" cy="16.5" r="15.5"/><path d="M10 19 V16 A6.5 6.5 0 0 1 23 16 V19"/><rect x="9" y="17" width="3" height="5" rx="1"/><rect x="21" y="17" width="3" height="5" rx="1"/><path d="M22.5 22 Q22 25 18 25"/></svg></a>
    </nav>
    <div class="phone">555-014-2297
      <svg width="16" height="16" viewBox="0 0 16 16" fill="none" stroke="#fff" stroke-width="1.6"><path d="M3 2 L6 2 L7 5 L5 6.5 Q6.5 9.5 9.5 11 L11 9 L14 10 L14 13 Q8 14 4 9 Q2 5 3 2Z"/></svg>
    </div>
  </header>

  <div class="hero" role="img" aria-label="Photo of a smiling woman jumping mid-air on a beach with the sea and blue sky behind her"></div>

  <div class="tagline">A SMALL TEAM OF DESIGNERS AND DEVELOPERS,<br>WHO HELP BRANDS WITH BIG IDEAS.</div>

  <section class="services">
    <div class="photo photo-pills" role="img" aria-label="Photo of assorted pills, capsules and medical tape on a table"></div>
    <article class="service service-patients">
      <h2>PATIENTS ADVOCACY<br>GROUPS</h2>
      <div class="rule"></div>
      <p>It has survived not only five centuries, but also the leap into electronic typesetting, remaining essentially unchanged.</p>
      <a class="more">READ MORE</a>
      <span class="pointer pointer-down"></span>
    </article>
    <div class="photo photo-scope" role="img" aria-label="Close-up photo of a laboratory microscope with a glass slide"></div>
    <article class="service service-pharma">
      <span class="pointer pointer-up-teal"></span>
      <h2>PHARMACEUTICAL<br>COMPANIES</h2>
      <div class="rule"></div>
      <p>It has survived not only five centuries, but also the leap into electronic typesetting, remaining essentially unchanged.</p>
      <a class="more">READ MORE</a>
    </article>
    <div class="photo photo-doctor" role="img" aria-label="Photo of a doctor's hands in a white coat holding a stethoscope"></div>
    <article class="service service-societies">
      <span class="pointer pointer-up-purple"></span>
      <h2>MEDICAL<br>SOCIETIES</h2>
      <div class="rule"></div>
      <p>It has survived not only five centuries, but also the leap into electronic typesetting, remaining essentially unchanged.</p>
      <a class="more">READ MORE</a>
    </article>
  </section>

  <div class="footer-tab">brivocell</div>
  <footer class="site-footer">
    <div class="address">No.##, ## street, Larkford, US</div>
    <div class="legal">© 2014<br>Privacy Policy</div>
    <div class="social" aria-label="Social links">
      <span class="s1"></span><span class="s2"></span><span class="s3"></span><span class="s4"></span>
    </div>
  </footer>
</body>
</html>
```